Web Design Services Create a Similar website to my Competitor

We would like a similar website designed like our main competitor with all the features there website has and more. Also we would like to accept payments through our website and to rank quickly with seo based on our home page and other page use of high traffic keywords. this is the website we would like to have ours designed similar to https://www.festivalpaintnook.com. we will be providing the same services and more just at a different location. We would also like to know be able to easily make adjustments to the website when its time to edit it please thanks.

Basically I am looking to have have similar website built almost exactly the same but with my logo, and other personalized information to my company Darla Parade Beauty Lounge. I will need to send you model images and logo design idea but the body and user interface of my competitor https://www.festivalpaintnook.com will be exactly the same. I can be reached anytime to answer any questions you may have.
Updates

Hi Designers I would like to clarify some information Festival Paint Nook is my Competitor we are not affiliated. I would like my website to be designed similar to hers but please do not take any content from her website to put on mine I will be providing images to be posted on my website. Also please do not use any of her videos or YouTube videos on my website to avoid any legal issues. Thanks for your understanding.

Target Market(s)

Make up Application Services For Events and Trinidad and Tobago Carnival

Industry/Entity Type

Beauty and Makeup Application and services

Coding

Coded - Design and coding required

Number of Pages Required

5+ page

Font styles to use
Sans Serif

Colors
E54698
E96AAD
F1A4CE
F9D9EA
FCEFF6
A7469A
B969AE
D3A5CF
EDDBEB
F8F0F9

Requirements
Must have
• Must be similar to my competitor, need a video section, testimonial and must be easily able to navigate to information sections and book now payment notifications running on all pages so customers can easily book there spot for 2026 carnival
Nice to have
• I am looking to have a similar website to https://www.festivalpaintnook.com created but make it as minimal and modern
Should not have
• Project can be coded if it makes it easier to create a similar look to my competitor just ask that updates can easily be made later on.

```html
<!DOCTYPE html>
<html lang="en">
<head>
<meta charset="utf-8">
<title>Darla Parade Beauty Lounge</title>
<link href="https://fonts.googleapis.com/css2?family=Passion+One:wght@400;700&family=Montserrat:wght@400;500;600;700&display=swap" rel="stylesheet">
<style>
:root{
  --pink:#E54698;--pink-2:#E96AAD;--pink-3:#F1A4CE;--pink-4:#F9D9EA;--pink-5:#FCEFF6;
  --plum:#A7469A;--plum-2:#B969AE;--plum-3:#D3A5CF;--plum-4:#EDDBEB;--plum-5:#F8F0F9;
  --ink:#333;--muted:#666;--dark:#0e0e10;--marble:#f4f3f4;
}
*{box-sizing:border-box;margin:0;padding:0}
html,body{width:1200px;height:5391px;overflow:hidden}
body{font-family:"Montserrat",sans-serif;color:var(--ink);background:#fff;font-size:11px}
.display{font-family:"Passion One",sans-serif;font-weight:400;color:var(--pink);letter-spacing:.5px}
section,header,footer{position:relative;width:1200px}
.abs{position:absolute}
.btn{position:absolute;display:flex;align-items:center;justify-content:center;background:var(--pink);color:#fff;font-size:10px;font-weight:600;border:2px solid #fff;box-shadow:0 0 0 1px var(--pink)}
.btn.ghost{background:transparent;border:1.5px solid #fff;box-shadow:none}
.img{position:absolute}
.title{position:absolute;left:0;width:100%;text-align:center;font-size:30px}

/* nav */
.nav{height:42px;background:#fff}
.nav .brand{left:121px;top:9px;font-size:20px}
.nav ul{list-style:none;position:absolute;left:530px;top:14px;display:flex;gap:22px;font-size:10px}
.nav li.active{color:var(--pink);border-bottom:1px solid var(--pink)}
.nav .btn{left:984px;top:7px;width:94px;height:28px;box-shadow:none;border:none}

/* hero */
.hero{height:601px;background:radial-gradient(ellipse at 50% 45%,#d7a08a 0 8%,#7b2a6e 22%,#4a1a6a 45%,#8a1f8f 70%,#2b0f3a 100%)}
.hero .photo{inset:0}
.hero h1{position:absolute;top:388px;width:100%;text-align:center;color:#fff;font-size:56px}
.hero p{position:absolute;top:452px;width:100%;text-align:center;color:#fff;font-size:13px}
.hero .btn{top:490px;height:34px;font-size:10px}

/* about */
.about{height:536px;background:linear-gradient(135deg,#fafafa,#f0eff0 50%,#fbfbfb)}
.about .photo{left:121px;top:63px;width:444px;height:326px;background:linear-gradient(120deg,#f2c21a,#e23b2e 40%,#7a3a1c 60%,#9e3aa0)}
.about .panel{left:565px;top:105px;width:513px;height:368px;background:linear-gradient(160deg,var(--pink-4),var(--pink-5) 60%,#fff);border:1px solid var(--pink-4)}
.about .tri{left:527px;top:330px}
.about h2{left:600px;top:130px;font-size:29px}
.about p{position:absolute;left:600px;width:450px;font-size:9.6px;line-height:18px;color:var(--muted)}
.about .btn{left:605px;top:404px;width:142px;height:30px}

/* services */
.services{height:492px;background:linear-gradient(180deg,#fde7f2,#fff 40%,#fde7f2)}
.services .title{top:48px}
.svc{position:absolute;top:119px;width:306px;height:203px}
.svc .tag{position:absolute;right:8px;top:12px;background:#fff;color:var(--pink);font-size:10px;font-weight:600;padding:3px 6px}
.svc .label{position:absolute;left:26px;top:182px;width:254px;height:66px;background:#fff;box-shadow:0 2px 8px rgba(0,0,0,.12);display:flex;align-items:center;justify-content:center;font-size:20px;color:var(--pink)}
.svc .label i{position:absolute;right:14px;top:28px;width:20px;height:20px;border-radius:50%;background:var(--pink)}
.arrow{position:absolute;width:12px;height:18px}
.services .more{left:238px;top:375px;color:var(--pink);font-size:10px}
.services .btn{left:538px;top:400px;width:124px;height:34px}

/* gallery */
.gallery{height:586px;background:linear-gradient(160deg,#f9f9f9,#efefef 50%,#fafafa)}
.gallery .title{top:62px}

/* packages */
.packages{height:584px;background:linear-gradient(180deg,var(--pink-3),var(--pink-2) 60%,#ec87bd)}
.packages .title{top:56px;color:#fff}
.pkg{position:absolute;background:#fff;box-shadow:0 2px 10px rgba(0,0,0,.1)}
.pkg .head{position:absolute;left:10px;top:10px;right:10px;height:86px;background:#f2eef1;display:flex;align-items:center;justify-content:center;text-align:center;font-size:14px;line-height:17px}
.pkg.feature .head{background:var(--plum-2);color:#fff;font-size:19px}
.pkg .price{position:absolute;left:32px;top:120px;color:var(--pink);font-size:28px}
.pkg .price small{font-size:10px;color:var(--ink);margin-left:6px}
.pkg .inc{position:absolute;left:32px;top:172px;font-size:11px}
.pkg ul{position:absolute;left:32px;top:204px;list-style:none;font-size:10px;line-height:22px}
.pkg li::before{content:"✓";color:var(--ink);margin-right:8px;font-weight:700}
.pkg.feature li::before{color:var(--pink)}
.pkg .btn{left:32px;width:240px;height:34px}

/* video */
.video{height:593px;background:linear-gradient(160deg,#fafafa,#eee)}
.video .photo{left:121px;top:64px;width:957px;height:389px;background:linear-gradient(90deg,#6d6a6e,#c9c2c0 40%,#4b4646 70%,#a89e9a)}
.video .play{left:578px;top:219px;width:44px;height:44px;border-radius:50%;background:rgba(255,255,255,.6)}
.video .frame{left:228px;top:356px;width:744px;height:188px;border:1px solid var(--pink-3)}
.video .box{left:243px;top:342px;width:714px;height:188px;background:linear-gradient(180deg,var(--pink-2),var(--plum-2));text-align:center;color:#fff}
.video .box h2{font-size:29px;color:#fff;margin-top:22px}
.video .box p{font-size:9.6px;line-height:15px;margin:12px auto 0;width:560px}

/* testimonials */
.reviews{height:576px;background:linear-gradient(160deg,#fbfbfb,#efefef)}
.reviews .title{left:-200px;top:69px}
.review{position:absolute;top:136px;width:306px;height:325px;background:#fff;box-shadow:0 2px 10px rgba(0,0,0,.08);padding:40px 24px 0}
.review .q{position:absolute;left:24px;top:-14px;font-family:"Passion One",sans-serif;font-size:60px;color:var(--pink-4);line-height:1}
.review .stars{color:#f5a623;font-size:12px;letter-spacing:1px}
.review .mark{position:absolute;right:20px;top:22px;width:22px;height:22px;border-radius:50%;background:var(--plum-3)}
.review p{margin-top:14px;font-size:10px;line-height:22px;color:var(--muted)}
.who{position:absolute;top:487px;display:flex;align-items:center;gap:12px;font-size:11px}
.who i{width:38px;height:38px;border-radius:50%;border:2px solid var(--pink);background:var(--pink-5)}
.who small{font-size:8px;color:var(--muted)}
.reviews .portrait{left:820px;top:0;width:258px;height:419px;background:linear-gradient(180deg,#fff,#f2d8cf 30%,#c98a62 60%,#f7f0ee)}
.reviews .btn{left:826px;top:438px;width:152px;height:34px}

/* cta */
.cta{height:220px;background:linear-gradient(90deg,var(--pink-2),var(--pink) 50%,var(--pink-2));text-align:center;color:#fff}
.cta h2{padding-top:50px;font-size:31px;color:#fff}
.cta p{margin-top:6px;font-size:10px}
.cta .btn{top:132px;height:36px}
.cta .btn.light{background:#fff;color:var(--pink);box-shadow:none;border:1px solid #fff}

/* faq */
.faq{height:586px;background:linear-gradient(160deg,#fbfbfb,#f1f1f1)}
.faq .title{top:60px}
.qa{position:absolute;left:197px;width:808px;height:42px;border:1px solid var(--pink-3);background:#fff;display:flex;align-items:center}
.qa .n{width:110px;height:100%;background:var(--pink-4);display:flex;align-items:center;justify-content:center;font-family:"Passion One",sans-serif;font-style:normal;color:var(--pink);font-size:26px}
.qa .t{margin-left:28px;font-size:12px}
.qa .chev{position:absolute;right:14px;top:16px}
.qa.open{height:80px;background:var(--pink-2);border:none;color:#fff;align-items:stretch}
.qa.open .n{background:var(--pink-3);color:#fff;height:80px}
.qa.open .body{margin-left:28px;padding-top:16px}
.qa.open .body p{font-size:9.6px;line-height:13px;margin-top:10px;width:640px}
.faq .btn{left:542px;top:526px;width:116px;height:34px}

/* reels */
.reels{height:283px;background:linear-gradient(160deg,#fbfbfb,#efefef)}
.reel{position:absolute;top:28px;width:184px;height:192px}
.reel i{position:absolute;left:78px;top:82px;width:28px;height:28px;border-radius:50%;background:rgba(255,255,255,.55)}

/* footer */
.foot{height:292px;background:var(--dark);color:#ddd}
.foot h4{position:absolute;top:62px;font-family:"Passion One",sans-serif;font-weight:400;font-size:15px;color:#fff}
.foot .brand{left:121px;top:54px;font-size:30px;position:absolute}
.foot .blurb{position:absolute;left:121px;top:104px;width:180px;font-size:8.6px;line-height:16px}
.foot ul{position:absolute;list-style:none;font-size:8.6px;line-height:18px}
.foot .row{position:absolute;display:flex;align-items:center;gap:14px;font-size:8.6px;line-height:13px}
.foot .row i{width:26px;height:26px;border-radius:50%;background:#fff;flex:none}
.foot .email{position:absolute;left:882px;top:142px;width:196px;height:36px;border:1px solid #888;font-size:8px;padding:12px 14px}
.foot .btn{left:882px;top:196px;width:124px;height:34px;border:none;box-shadow:none}
.foot .copy{position:absolute;top:270px;width:100%;text-align:center;font-size:8px}
</style>
</head>
<body>

<header class="nav">
  <div class="abs brand display">Darla Parade Beauty Lounge</div>
  <ul><li class="active">Home</li><li>Services</li><li>Booking</li><li>FAQ</li><li>Contact</li></ul>
  <a class="btn">Book Now</a>
</header>

<section class="hero">
  <div class="img photo" role="img" aria-label="Close-up of a carnival model in a purple and magenta feathered headdress"></div>
  <h1 class="display">Get Carnival-Ready with Darla Glam</h1>
  <p>Professional Makeup Services for Carnival, Weddings &amp; Special Events.</p>
  <a class="btn" style="left:462px;width:150px">Book Your Glam Now</a>
  <a class="btn ghost" style="left:622px;width:120px">View Services</a>
</section>

<section class="about">
  <div class="img photo" role="img" aria-label="Two carnival performers in yellow, red and purple feathered costumes"></div>
  <div class="abs panel"></div>
  <svg class="abs tri" width="40" height="150"><polygon points="38,0 38,150 0,150" fill="var(--plum-3)"/></svg>
  <h2 class="abs display">About Darla Parade Beauty Lounge</h2>
  <p style="top:174px">At Darla Parade Beauty Lounge, we don't just do makeup — we create transformational beauty experiences that celebrate confidence, creativity, and Caribbean culture. Founded with a deep love for Carnival and a passion for flawless artistry, our studio specializes in high-impact, long-lasting makeup looks for Trinidad and Tobago Carnival, weddings, photoshoots, and special events.</p>
  <p style="top:284px">With a personalized, client-first approach, Darla and her team of certified makeup artists are known for delivering radiant glam that holds up through dancing, heat, and the vibrant energy of the road. Whether you're a Carnival queen, a blushing bride, or just want to turn heads at your next event, we're here to make you feel bold, beautiful, and unforgettable.</p>
  <a class="btn">Book Your Glam Now</a>
</section>

<section class="services">
  <h2 class="title display">Our Services</h2>
  <svg class="arrow" style="left:84px;top:254px" viewBox="0 0 12 18"><path d="M10 2 3 9l7 7" stroke="var(--pink)" stroke-width="2" fill="none"/></svg>
  <svg class="arrow" style="left:1096px;top:254px" viewBox="0 0 12 18"><path d="M2 2l7 7-7 7" stroke="var(--pink)" stroke-width="2" fill="none"/></svg>
  <div class="svc" style="left:121px">
    <div class="img" role="img" aria-label="Carnival glam makeup look with rhinestones" style="inset:0;background:linear-gradient(160deg,#9aa0a8,#5f4a57 50%,#c9a9b8)"></div>
    <span class="tag">193.50US</span>
    <div class="label">Carnival Glam<i></i></div>
  </div>
  <div class="svc" style="left:447px">
    <div class="img" role="img" aria-label="Bridal glam makeup with jewelled headpiece" style="inset:0;background:linear-gradient(160deg,#cfc7b8,#e8d8c8 50%,#a89a86)"></div>
    <span class="tag">400USD</span>
    <div class="label">Bridal Glam<i></i></div>
  </div>
  <div class="svc" style="left:773px">
    <div class="img" role="img" aria-label="Group of carnival masqueraders in colourful feathers" style="inset:0;background:linear-gradient(120deg,#d8d6d2,#e0457e 40%,#e8c12a 70%,#c53c9c)"></div>
    <span class="tag">143USD/person</span>
    <div class="label">Group Bookings<i></i></div>
  </div>
  <span class="abs more">View More →</span>
  <a class="btn">View All Services</a>
</section>

<section class="gallery">
  <h2 class="title display">Photo Gallery</h2>
  <div class="img" role="img" aria-label="Carnival performer in an orange jewelled costume with a white feather backpiece" style="left:121px;top:128px;width:306px;height:395px;background:linear-gradient(170deg,#ddd,#c0591f 45%,#3a2518)"></div>
  <div class="img" role="img" aria-label="Model with a pink and purple feathered headdress" style="left:447px;top:128px;width:306px;height:250px;background:linear-gradient(150deg,#eee,#b42a9a 40%,#7a2aa8 70%,#e8e8e8)"></div>
  <div class="img" role="img" aria-label="Woman wearing a red masquerade mask" style="left:447px;top:387px;width:306px;height:136px;background:linear-gradient(90deg,#2b2a1a,#b8232c 50%,#1c1a12)"></div>
  <div class="img" role="img" aria-label="Group of masqueraders in bright feathers in a studio" style="left:773px;top:128px;width:305px;height:395px;background:linear-gradient(160deg,#ddd,#8a2a9a 35%,#e2c51c 65%,#7a3d1e)"></div>
</section>

<section class="packages">
  <h2 class="title display">Carnival Packages</h2>
  <svg class="arrow" style="left:92px;top:266px" viewBox="0 0 12 18"><path d="M10 2 3 9l7 7" stroke="#6a1a4a" stroke-width="2" fill="none"/></svg>
  <svg class="arrow" style="left:1096px;top:266px" viewBox="0 0 12 18"><path d="M2 2l7 7-7 7" stroke="#6a1a4a" stroke-width="2" fill="none"/></svg>
  <div class="pkg" style="left:121px;top:141px;width:306px;height:362px">
    <div class="head">Road-Ready<br>Glam Package</div>
    <div class="price">400<small>USD</small></div>
    <div class="inc">Includes:</div>
    <ul><li>Full Carnival makeup application</li><li>Face gems &amp; glitter accents</li><li>Lashes included</li><li>Setting spray for long wear</li></ul>
    <a class="btn" style="top:314px">Book Now</a>
  </div>
  <div class="pkg feature" style="left:447px;top:124px;width:306px;height:396px">
    <div class="head">Group Carnival Glam</div>
    <div class="price">143<small>USD/person</small></div>
    <div class="inc">Includes:</div>
    <ul><li>Road Ready Glam for each group member</li><li>Mobile service to your location</li><li>FREE touch-up kits for all</li><li>Discounted group pricing</li></ul>
    <a class="btn" style="top:340px">Book Now</a>
  </div>
  <div class="pkg" style="left:773px;top:141px;width:306px;height:362px">
    <div class="head">Add-On Services:</div>
    <div class="price">400<small>USD</small></div>
    <div class="inc">Includes:</div>
    <ul><li>Rhinestone artistry &amp; custom face gems</li><li>Glitter body art</li><li>Carnival hairstyling (optional)</li><li>On-site touch-up service for the road</li></ul>
    <a class="btn" style="top:310px">Book Now</a>
  </div>
</section>

<section class="video">
  <div class="img photo" role="img" aria-label="Video still of makeup artists preparing clients in a studio"></div>
  <div class="abs play"></div>
  <svg class="abs" style="left:595px;top:232px" width="14" height="18"><polygon points="0,0 14,9 0,18" fill="var(--pink)"/></svg>
  <div class="abs frame"></div>
  <div class="abs box">
    <h2 class="display">Behind the Glam</h2>
    <p>Experience the magic of Darla Parade Beauty Lounge in motion. From flawless skin prep to bold glitter and lashes, watch our expert glam team bring Carnival and events looks to life.</p>
    <p>Whether it's your first time on the road or your fifth, see why our clients trust us to deliver confidence, beauty, and Carnival-ready perfection — every time.</p>
  </div>
</section>

<section class="reviews">
  <div class="img portrait" role="img" aria-label="Model wearing a blue and pink masquerade mask"></div>
  <h2 class="title display">What Our Clients Say</h2>
  <svg class="arrow" style="left:80px;top:290px" viewBox="0 0 12 18"><path d="M10 2 3 9l7 7" stroke="var(--plum)" stroke-width="2" fill="none"/></svg>
  <svg class="arrow" style="left:768px;top:290px" viewBox="0 0 12 18"><path d="M2 2l7 7-7 7" stroke="var(--plum)" stroke-width="2" fill="none"/></svg>
  <div class="review" style="left:121px">
    <span class="q">❝</span><i class="mark"></i>
    <div class="stars">★★★★★</div>
    <p>"Working with Darla Parade Beauty Lounge was an unforgettable experience from start to finish. I booked a Carnival makeup package for both Monday and Tuesday, and let me tell you — I've never looked or felt more stunning. From the moment I arrived, the vibe was welcoming, professional, and full of positive energy. Darla knew exactly how to bring my features while still keeping the vibrant, bold Carnival glam....</p>
  </div>
  <div class="review" style="left:447px">
    <span class="q">❝</span><i class="mark"></i>
    <div class="stars">★★★★★</div>
    <p>"My makeup stayed flawless through sun, sweat, and dancing — and the compliments didn't stop all day. Even photographers were asking who did my look! What I loved most was how the team made me feel: seen, celebrated, and confident. I wasn't just a client I was a queen for the day. I've already booked again for next year and recommended them to my entire crew. If you want to feel beautiful, empowered, and Carnival-ready, this....</p>
  </div>
  <div class="who" style="left:121px"><i></i><span>— <b>Renee M.</b> <small>Carnival 2024 Client</small></span></div>
  <div class="who" style="left:447px"><i></i><span>— <b>Keisha L.</b> <small>Port of Spain</small></span></div>
  <a class="btn">Book Your Glam Now</a>
</section>

<section class="cta">
  <div class="img" role="img" aria-label="Faint line-drawn flower pattern" style="inset:0;background:radial-gradient(circle at 10% 40%,rgba(255,255,255,.12),transparent 25%),radial-gradient(circle at 90% 60%,rgba(255,255,255,.12),transparent 25%)"></div>
  <h2 class="display" style="position:relative">Secure Your Spot Before It's Gone!</h2>
  <p style="position:relative">Book a quick call to get clear on your options &amp; how I can support you no pressure...</p>
  <a class="btn light" style="left:486px;width:84px">Book Now</a>
  <a class="btn ghost" style="left:582px;width:132px">View Glam Packages</a>
</section>

<section class="faq">
  <h2 class="title display">FAQ</h2>
  <div class="qa open" style="top:126px"><em class="n">01</em><div class="body"><b style="font-weight:500;font-size:12px">What types of makeup services do you offer?</b><p>We specialize in bold Carnival glam, soft glam for events, bridal makeup, and group bookings. Whether you're hitting the road for Carnival or celebrating a special moment, we've got the perfect look for you.</p></div>
    <svg class="chev" width="12" height="8"><path d="M1 7l5-5 5 5" stroke="#fff" stroke-width="1.5" fill="none"/></svg></div>
  <div class="qa" style="top:243px"><em class="n">02</em><span class="t">How do I book an appointment?</span><svg class="chev" width="12" height="8"><path d="M1 1l5 5 5-5" stroke="#333" stroke-width="1.5" fill="none"/></svg></div>
  <div class="qa" style="top:297px"><em class="n">03</em><span class="t">How early should I book for Carnival?</span><svg class="chev" width="12" height="8"><path d="M1 1l5 5 5-5" stroke="#333" stroke-width="1.5" fill="none"/></svg></div>
  <div class="qa" style="top:352px"><em class="n">04</em><span class="t">Do I need to pay in advance?</span><svg class="chev" width="12" height="8"><path d="M1 1l5 5 5-5" stroke="#333" stroke-width="1.5" fill="none"/></svg></div>
  <div class="qa" style="top:406px"><em class="n">05</em><span class="t">What's included in the glam packages?</span><svg class="chev" width="12" height="8"><path d="M1 1l5 5 5-5" stroke="#333" stroke-width="1.5" fill="none"/></svg></div>
  <div class="qa" style="top:461px"><em class="n">06</em><span class="t">Can I book for a group or bridal party?</span><svg class="chev" width="12" height="8"><path d="M1 1l5 5 5-5" stroke="#333" stroke-width="1.5" fill="none"/></svg></div>
  <a class="btn">View All FAQ</a>
</section>

<section class="reels">
  <div class="reel" style="left:121px"><div class="img" role="img" aria-label="Video still of a carnival makeup look in red" style="inset:0;background:linear-gradient(160deg,#5a1a3a,#c0304a 50%,#2a0d1a)"></div><i></i></div>
  <div class="reel" style="left:313px"><div class="img" role="img" aria-label="Video still of a model in a blue headpiece" style="inset:0;background:linear-gradient(160deg,#1a2a4a,#8a2a7a 50%,#1a1a2a)"></div><i></i></div>
  <div class="reel" style="left:506px"><div class="img" role="img" aria-label="Video still of a gold masquerade look" style="inset:0;background:linear-gradient(160deg,#3a2a1a,#9a7a4a 50%,#1a120a)"></div><i></i></div>
  <div class="reel" style="left:698px"><div class="img" role="img" aria-label="Video still of pink and orange studio lighting" style="inset:0;background:linear-gradient(160deg,#f08a2a,#e0408a 50%,#7a2aa0)"></div><i></i></div>
  <div class="reel" style="left:892px"><div class="img" role="img" aria-label="Video still of colourful carnival face art" style="inset:0;background:linear-gradient(160deg,#e05a2a,#d0408a 40%,#3a8ad0 80%)"></div><i></i></div>
</section>

<footer class="foot">
  <div class="brand display">Darla Glam</div>
  <p class="blurb">At Darla Parade Beauty Lounge, we don't just do makeup — we create transformational beauty experiences that celebrate confidence,...</p>
  <h4 style="left:348px">Quick Links</h4>
  <ul style="left:348px;top:98px"><li>Home</li><li>About Us</li><li>Services</li><li>Glam Packages</li><li>Gallery</li><li>Contact</li></ul>
  <h4 style="left:505px">Contact Us</h4>
  <div class="row" style="left:505px;top:104px"><svg width="26" height="26"><circle cx="13" cy="13" r="13" fill="#fff"/><path d="M13 6a5 5 0 0 0-5 5c0 4 5 9 5 9s5-5 5-9a5 5 0 0 0-5-5z" fill="var(--dark)"/></svg><span>Marlon T. Greaves, Esq.<br>210 Harbour Road, 4th Floor<br>Port of Spain</span></div>
  <div class="row" style="left:505px;top:150px"><svg width="26" height="26"><circle cx="13" cy="13" r="13" fill="#fff"/><path d="M9 7h3l1 3-2 1a7 7 0 0 0 3 3l1-2 3 1v3c-6 0-9-3-9-9z" fill="var(--dark)"/></svg><span>+1 (868) 555-0142</span></div>
  <div class="row" style="left:505px;top:182px"><svg width="26" height="26"><circle cx="13" cy="13" r="13" fill="#fff"/><path d="M7 13l12-5-4 11-2-4z" fill="var(--dark)"/></svg><span style="color:var(--pink)">hello@darlaparadebeauty.com</span></div>
  <h4 style="left:741px">Community</h4>
  <div class="row" style="left:741px;top:100px"><i></i><span>Fanpage</span></div>
  <div class="row" style="left:741px;top:140px"><i></i><span>Updates</span></div>
  <div class="row" style="left:741px;top:180px"><i></i><span>Network</span></div>
  <h4 style="left:882px">Subscribe Newsletter</h4>
  <p style="position:absolute;left:882px;top:106px;font-size:8.6px">Subscribe to our newsletter</p>
  <div class="email">Enter email...</div>
  <a class="btn">Subscribe</a>
  <p class="copy">© 2025 Darla Parade Beauty Lounge . All Rights Reserved.</p>
</footer>

</body>
</html>
```